Bus Wrap partial

For the design, I have attached some images and some examples of current design but we want to update images, wording and the design in that design you have been doing for us. No need to use all images just the ones you think work
Include the playmark logo on one side
To include
pip & clover logo on all sides
on the sides of the bus add below messaging words in a triangle design
All inclusive
Incursions
Excursions
CTA & Tagline on all sides
TOUR NOW
Premium Education & Care
6 weeks- 6 years
On the back include
Logo
Tagline
TOUR NOW
Premium Education & Care
6 weeks- 6 years
All inclusive (under that have)
Clover Curriculum logo
Bloom + logo
Haven + logo
Tandem logo
pipandclover.edu.au
Bus type- 1/2016 Varoka Tessan Rover 15 Seater minibus 3.0 Turbo Diesel - automatic transmission Vin: KRMZX48Q711093452 Engine: 2QV4817365 Colour: White

```html
<!DOCTYPE html>
<html lang="en">
<head>
<meta charset="utf-8">
<title>pip &amp; clover — Bus Wrap Sides</title>
<link rel="stylesheet" href="https://fonts.googleapis.com/css2?family=Patrick+Hand&display=swap">
<style>
  :root {
    --wrap-blue: #1a6fc0;
    --wrap-navy: #16357a;
    --wrap-green: #4fb32f;
    --wrap-green-light: #8ccc2e;
    --wrap-yellow: #e9d81a;
    --wrap-white: #ffffff;
    --panel-edge: #d6dbe1;
    --ink-blue: #1d68b5;
    --ink-dark: #1e1e1e;
    --canvas-bg: #eef1f4;
    --photo-warm: #c9a57e;
    --photo-green: #7fa85a;
    --photo-lab: #b9b4c8;
    --photo-play: #d9b98c;
  }
  html, body {
    margin: 0;
    padding: 0;
    overflow: hidden;
  }
  body {
    width: 1200px;
    height: 1132px;
    background: var(--canvas-bg);
  }
  .wrap-sheet {
    display: flex;
    flex-direction: column;
    width: 1200px;
    height: 1132px;
  }
  .wrap-side {
    display: block;
    width: 1200px;
    height: 566px;
  }
  .hand {
    font-family: "Patrick Hand", "Comic Sans MS", cursive;
  }
  .brand-name {
    font-size: 96px;
    fill: var(--wrap-white);
  }
  .tagline {
    font-size: 38px;
    fill: var(--wrap-white);
  }
  .cta-title {
    font-size: 34px;
    fill: var(--ink-blue);
  }
  .cta-line {
    font-size: 21px;
    fill: var(--ink-blue);
  }
  .cta-url {
    font-size: 21px;
    fill: var(--ink-dark);
  }
</style>
</head>
<body>
<main class="wrap-sheet">

  <!-- Kerb side: cab on the left -->
  <svg class="wrap-side wrap-side--left" viewBox="0 0 1200 566" xmlns="http://www.w3.org/2000/svg">
    <rect class="body-panel" x="20" y="30" width="1160" height="500" rx="40" fill="var(--wrap-white)" stroke="var(--panel-edge)" stroke-width="2"/>
    <path class="field-blue" d="M600 30 H1140 Q1180 30 1180 70 V490 Q1180 530 1140 530 H380 C420 400 470 250 600 30 Z" fill="var(--wrap-blue)"/>
    <path class="stripe-navy" d="M585 30 C470 240 420 400 372 530" fill="none" stroke="var(--wrap-navy)" stroke-width="12"/>
    <path class="stripe-yellow" d="M630 30 C600 70 580 100 560 130" fill="none" stroke="var(--wrap-yellow)" stroke-width="16"/>
    <path class="band-navy" d="M420 470 C560 360 880 320 1180 292" fill="none" stroke="var(--wrap-navy)" stroke-width="14"/>
    <path class="field-green" d="M410 490 C560 380 880 338 1180 306 V490 Q1180 530 1140 530 H395 Z" fill="var(--wrap-green)"/>
    <path class="field-green-light" d="M395 530 C600 450 900 420 1180 410 V490 Q1180 530 1140 530 Z" fill="var(--wrap-green-light)"/>

    <circle cx="530" cy="210" r="96" fill="var(--wrap-white)"/>
    <circle class="photo-frame" cx="530" cy="210" r="84" fill="var(--photo-lab)" stroke="var(--wrap-yellow)" stroke-width="7" role="img" aria-label="Photo: a young child in a lab coat building with coloured blocks"/>
    <circle cx="490" cy="370" r="92" fill="var(--wrap-white)"/>
    <circle class="photo-frame" cx="490" cy="370" r="80" fill="var(--photo-green)" stroke="var(--wrap-yellow)" stroke-width="7" role="img" aria-label="Photo: a child in a sun hat tending plants in a garden"/>

    <g class="brand">
      <text class="hand brand-name" x="650" y="200" textLength="410" lengthAdjust="spacingAndGlyphs">pip &amp; clover</text>
      <circle cx="1112" cy="168" r="28" fill="var(--wrap-yellow)"/>
    </g>

    <text class="hand tagline" x="595" y="420" transform="rotate(-6 595 420)" textLength="550" lengthAdjust="spacingAndGlyphs">• All inclusive • Incursions • Excursions</text>

    <g class="cta">
      <text class="hand cta-title" x="180" y="300">TOUR NOW</text>
      <text class="hand cta-line" x="180" y="325">Premium Education &amp; Care</text>
      <text class="hand cta-line" x="180" y="347">6 weeks- 6 years</text>
      <text class="hand cta-url" x="180" y="378">pipandclover.edu.au</text>
    </g>
  </svg>

  <!-- Road side: cab on the right -->
  <svg class="wrap-side wrap-side--right" viewBox="0 0 1200 566" xmlns="http://www.w3.org/2000/svg">
    <rect class="body-panel" x="20" y="30" width="1160" height="500" rx="40" fill="var(--wrap-white)" stroke="var(--panel-edge)" stroke-width="2"/>
    <g class="livery" transform="translate(1200 0) scale(-1 1)">
      <path class="field-blue" d="M600 30 H1140 Q1180 30 1180 70 V490 Q1180 530 1140 530 H380 C420 400 470 250 600 30 Z" fill="var(--wrap-blue)"/>
      <path class="stripe-navy" d="M585 30 C470 240 420 400 372 530" fill="none" stroke="var(--wrap-navy)" stroke-width="12"/>
      <path class="stripe-yellow" d="M630 30 C600 70 580 100 560 130" fill="none" stroke="var(--wrap-yellow)" stroke-width="16"/>
      <path class="band-navy" d="M420 470 C560 360 880 320 1180 292" fill="none" stroke="var(--wrap-navy)" stroke-width="14"/>
      <path class="field-green" d="M410 490 C560 380 880 338 1180 306 V490 Q1180 530 1140 530 H395 Z" fill="var(--wrap-green)"/>
      <path class="field-green-light" d="M395 530 C600 450 900 420 1180 410 V490 Q1180 530 1140 530 Z" fill="var(--wrap-green-light)"/>
    </g>

    <circle cx="670" cy="205" r="96" fill="var(--wrap-white)"/>
    <circle class="photo-frame" cx="670" cy="205" r="84" fill="var(--photo-warm)" stroke="var(--wrap-yellow)" stroke-width="7" role="img" aria-label="Photo: a child in a yellow shirt patting a goat at a farm"/>
    <circle cx="710" cy="375" r="92" fill="var(--wrap-white)"/>
    <circle class="photo-frame" cx="710" cy="375" r="80" fill="var(--photo-play)" stroke="var(--wrap-yellow)" stroke-width="7" role="img" aria-label="Photo: a child looking through a magnifying glass in a playroom"/>

    <g class="brand">
      <text class="hand brand-name" x="60" y="200" textLength="410" lengthAdjust="spacingAndGlyphs">pip &amp; clover</text>
      <circle cx="522" cy="168" r="28" fill="var(--wrap-yellow)"/>
    </g>

    <text class="hand tagline" x="60" y="340" transform="rotate(6 60 340)" textLength="510" lengthAdjust="spacingAndGlyphs">• All inclusive • Incursions • Excursions</text>

    <g class="cta" text-anchor="end">
      <text class="hand cta-title" x="1040" y="300">TOUR NOW</text>
      <text class="hand cta-line" x="1040" y="325">Premium Education &amp; Care</text>
      <text class="hand cta-line" x="1040" y="347">6 weeks- 6 years</text>
      <text class="hand cta-url" x="1040" y="378">pipandclover.edu.au</text>
    </g>
  </svg>

</main>
</body>
</html>
```